Movie poster for drama/thriller feature

We need a movie poster for an edgy microbudget, drama/thriller feature called Drifting Past the Quiet Harbour and is about a “night in the life” of an escort and her driver after she discovers that her mother, who was caring for her daughter, has died. She has just one night to raise the money to cover the arrears on her mother’s mortgage and return to collect her daughter before her very religious aunt calls Youth Shelter. On top of that she has to enlist the help of her new driver who is also very religious and hates her because she’s a “whore”. He is only doing this job because, as a Cuban refugee, he has had to take a job with his uncle, who is head of security at the agency, in order to pay him back what it cost to bring him to Canada. So, at the core of the story is this relationship between two people who hate each other but are stuck together in a car for an entire night. The third character is the uncle - head of security - who becomes increasingly "dark" and violent as the night goes on as he feels he is losing the loyalty of his nephew to a sex worker who is ripping off his boss.

So, that's the backdrop to the story.

Now, we want the poster to reflect that this is a scrappy, edgy little film, a bit controversial (just the title alone, obviously). Some of our inspiration for the poster are the kind of minimalist designs from French New Wave films (examples uploaded). The title itself can either be written out in toto or you could put the acronym in bold letters - DPTQH - with their meaning smaller below it. You can play with it, anyway, to come up with some cool. I've also included stills from the film of the three main characters - Lydia, the lead/star, Hector (her driver) and Alberto, the antaonist/uncle. You can crop these to make them work. I just left them full size so that you'd have more options.

If you have questions, don't hesitate to ask.

best
Derek

Target Market(s)

indie film goers, younger, city-based, hipster demographic

Industry/Entity Type

Film Production

Font styles to use
Sans Serif

Colors

Designer to choose colors to be used in the design.

Requirements
Must have
• A great look, the title, and some credits:
• tagline: one night can change your whole world
• A film by Marisol Tenbrook & Derek Almquist
• With
• Ilse Kortwijnen
• Tomas Echeverri-Lujan
• Ramon Ibarra Castellet
• Cinematography
• Gil Norbeck
• Produced by:
• Crooked Lantern Productions
• Fernhill Studios
• and a credit block with:
• Marisol Tenbrook ... co-producer
• Ilse Kortwijnen ... co-producer
• Tomas Echeverri-Lujan ... co-producer
• Brice Pettle ... co-producer
• Derek Almquist ... co-producer
• Editing by
• Jodie McCarran
• Production Design by
• Anselmo Dutra Queiroz
• Wendy Tolle ... key makeup artist
• Rosalind Mercado ... makeup artist Production Management
• Tess Garvely ... production manager Second Unit Director or Assistant Director
• Tess Garvely ... first assistant director Sound Department
• Neil Crampton ... sound editor
• Kevin Santoso ... sound recordist Stunts
• Ramon Ibarra Castellet ... action coordinator
• Gary Pelton ... still photographer
• Bethany Cole ... swing
• Priya Okonjo ... still photographer
• Daniela Ferrucci ... swing Costume and Wardrobe Department
• Nora Whitcombe ... wardrobe
• Milena Voska ... wardrobe supervisor Transportation Department
• Harriet Coyle ... craft service
• Ada Finch ... script supervisor
• Paolo Reyes ... production assistant
• Lucia Bermejo ... craft service

```html
<!DOCTYPE html>
<html lang="en">
<head>
<meta charset="utf-8">
<title>DPTQH — Drifting Past the Quiet Harbour</title>
<link href="https://fonts.googleapis.com/css2?family=Oswald:wght@400;500;700&family=Roboto+Condensed:wght@400;700&display=swap" rel="stylesheet">
<style>
  :root {
    --page: #ffffff;
    --butter: #fbe08f;
    --ink: #000000;
    --paper: #ffffff;
    --shade: #3a3320;
  }
  * { box-sizing: border-box; margin: 0; padding: 0; }
  html, body { width: 1200px; height: 1000px; overflow: hidden; background: var(--page); }
  .poster {
    position: absolute; left: 302px; top: 97px; width: 595px; height: 841px;
    background: var(--butter); overflow: hidden;
  }
  .still { position: absolute; }
  .still--lead {
    left: 22px; top: 108px; width: 168px; height: 532px;
    border-radius: 70px 70px 0 0;
    background: radial-gradient(ellipse at 50% 30%, #d9c27a 0%, #8a7a4c 55%, #2b2618 100%);
  }
  .still--driver {
    left: 322px; top: 205px; width: 273px; height: 435px;
    border-radius: 60px 30px 0 0;
    background: linear-gradient(180deg, #3a3320 0%, #111 35%, #000 100%);
  }
  .top-credits {
    position: absolute; left: 0; right: 0; top: 34px;
    font-family: "Roboto Condensed", sans-serif; font-size: 14px; line-height: 19.5px;
    color: var(--ink); text-align: center; white-space: nowrap;
  }
  .top-credits b { font-weight: 700; }
  .title-art { position: absolute; left: 0; top: 0; width: 595px; height: 640px; }
  .title-mark {
    font-family: "Oswald", sans-serif; font-weight: 700; fill: var(--paper);
  }
  .title-full {
    font-family: "Oswald", sans-serif; font-weight: 500; fill: var(--paper);
  }
  .title-shadow { fill: var(--shade); opacity: .6; }
  .tagline {
    font-family: "Oswald", sans-serif; font-weight: 400; fill: var(--paper);
    letter-spacing: 1px;
  }
  .credit-block {
    position: absolute; left: 0; bottom: 0; width: 595px; height: 201px;
    background: var(--ink); color: var(--paper);
    padding: 14px 16px 0 20px;
    font-family: "Oswald", sans-serif; font-weight: 400;
    font-size: 16px; line-height: 24px; text-transform: uppercase;
  }
  .name { white-space: nowrap; }
  .role {
    display: inline-block; vertical-align: middle;
    font-size: 5px; line-height: 5.5px; text-align: right;
    margin: 0 3px 0 5px; max-width: 44px; white-space: normal;
  }
</style>
</head>
<body>
<main class="poster">
  <div class="still still--lead" role="img" aria-label="Halftone still of Lydia, the lead, holding a handbag"></div>
  <div class="still still--driver" role="img" aria-label="Halftone still of Hector, her driver, in a dark jacket"></div>

  <p class="top-credits">
    A film by <b>Marisol Tenbrook &amp;</b><br>
    <b>Derek Almquist</b><br>
    With <b>Ilse Kortwijnen •</b><br>
    <b>Tomas Echeverri-Lujan • Ramon</b><br>
    <b>Ibarra Castellet</b> Cinematogra-<br>
    phy <b>Gil Norbeck</b><br>
    Produced by: <b>Crooked Lantern</b><br>
    <b>Productions Fernhill Studios</b>
  </p>

  <svg class="title-art" viewBox="0 0 595 640" aria-labelledby="film-title">
    <title id="film-title">DPTQH — Drifting Past the Quiet Harbour</title>
    <text class="title-mark" x="20" y="455" font-size="250" textLength="550" lengthAdjust="spacingAndGlyphs">DPTQH</text>
    <text class="title-full title-shadow" x="22" y="505" font-size="40" textLength="556" lengthAdjust="spacingAndGlyphs">Drifting Past the Quiet Harbour</text>
    <text class="title-full" x="20" y="503" font-size="40" textLength="556" lengthAdjust="spacingAndGlyphs">Drifting Past the Quiet Harbour</text>
    <text class="tagline" x="578" y="616" font-size="15" text-anchor="end">ONE NIGHT CAN CHANGE YOUR WHOLE WORLD</text>
  </svg>

  <section class="credit-block">
    <span class="role">Co-producer</span><span class="name">Marisol Tenbrook</span> • <span class="name">Ilse Kortwijnen</span> • <span class="name">Tomas Echeverri-Lujan</span> • <span class="name">Brice Pettle</span> • <span class="name">Derek Almquist</span> •
    <span class="role">Editing by</span><span class="name">Jodie McCarran</span>
    <span class="role">Production design by</span><span class="name">Anselmo Dutra Queiroz</span>
    <span class="role">Key makeup artist</span><span class="name">Wendy Tolle</span>
    <span class="role">Makeup artist production management</span><span class="name">Rosalind Mercado</span>
    <span class="role">Production manager second unit director</span><span class="name">Tess Garvely</span>
    <span class="role">First assistant director sound dept</span><span class="name">Tess Garvely</span>
    <span class="role">Sound editor</span><span class="name">Neil Crampton</span>
    <span class="role">Sound recordist stunts</span><span class="name">Kevin Santoso</span>
    <span class="role">Action coordinator</span><span class="name">Ramon Ibarra Castellet</span>
    <span class="role">Still photographer</span><span class="name">Gary Pelton</span>
    <span class="role">Swing</span><span class="name">Bethany Cole</span>
    <span class="role">Still photographer</span><span class="name">Priya Okonjo</span>
    <span class="role">Swing costume and wardrobe dept</span><span class="name">Daniela Ferrucci</span>
    <span class="role">Wardrobe</span><span class="name">Nora Whitcombe</span>
    <span class="role">Wardrobe supervisor</span><span class="name">Milena Voska</span>
    <span class="role">Craft service</span><span class="name">Harriet Coyle</span>
    <span class="role">Script supervisor</span><span class="name">Ada Finch</span>
    <span class="role">Production assistant</span><span class="name">Paolo Reyes</span>
    <span class="role">Craft service</span><span class="name">Lucia Bermejo</span>
  </section>
</main>
</body>
</html>
```